Postcard Design

We are Bluebridge care. A new way of providing quality healthcare for less. We offer a monthly membership program for $77 per person, $167 per family and cover about 85% of medical conditions. Medical office visits are just $7 each. This innovative program have already saved millions of dollars for it's members in health care costs. We are inviting people to a brief, educational meeting to learn more about how they can save money on their healthcare. We need something catchy and upbeat, positive with 1-2 photos inviting them to come find out more. We will be having appetizers. The date is Wednesday, Feb. 18 drop by between 6-8 pm
Industry/Entity Type
Healthcare

```html
<!DOCTYPE html>
<html lang="en">
<head>
<meta charset="utf-8">
<title>Bluebridge care – Postcard</title>
<link rel="stylesheet" href="https://fonts.googleapis.com/css2?family=Nunito+Sans:wght@300;400;700;800&display=swap">
<style>
  :root {
    --backdrop: #2b1022;
    --card: #ffffff;
    --brand-blue: #1184b9;
    --brand-orange: #f39323;
    --slate: rgba(70, 70, 74, 0.82);
    --ink-light: #ffffff;
    --muted: #8a8a8a;
    --rule: #b9b9b9;
    --photo-light: #f3ede7;
    --photo-warm: #d9b9a0;
    --photo-cool: #c9d6dc;
  }
  * { margin: 0; padding: 0; box-sizing: border-box; }
  html, body { width: 1200px; height: 841px; overflow: hidden; }
  body {
    position: relative;
    background: var(--backdrop);
    font-family: "Nunito Sans", Arial, sans-serif;
  }

  .postcard { position: absolute; background: var(--card); overflow: hidden; }

  /* Address side */
  .postcard--address { left: 33px; top: 37px; width: 689px; height: 551px; }
  .brand-name {
    position: absolute;
    color: var(--brand-blue);
    font-weight: 800;
    line-height: 1.05;
    text-align: center;
    white-space: nowrap;
  }
  .postcard--address .brand-name { left: 38px; top: 78px; width: 134px; font-size: 24px; }
  .bubble {
    position: absolute;
    border-radius: 50%;
    display: flex; align-items: center; justify-content: center;
    text-align: center;
    font-weight: 700;
    line-height: 1.2;
  }
  .bubble--invite { background: var(--brand-orange); color: var(--ink-light); left: 183px; top: 19px; width: 166px; height: 166px; font-size: 17px; }
  .bubble--date { background: var(--brand-blue); color: var(--ink-light); left: 338px; top: 15px; width: 148px; height: 148px; font-size: 17px; }
  .stamp-box {
    position: absolute; left: 575px; top: 40px; width: 97px; height: 106px;
    border: 1px dotted var(--muted);
    color: var(--muted); font-size: 17px; line-height: 1.2;
    display: flex; align-items: center; justify-content: center; text-align: center;
  }
  .address-photo { position: absolute; left: 2px; top: 191px; width: 320px; height: 268px; }
  .address-line { position: absolute; left: 382px; width: 300px; height: 1px; background: var(--rule); }

  /* Offer side */
  .postcard--offer { left: 435px; top: 232px; width: 717px; height: 551px; }
  .offer-art { position: absolute; inset: 0; width: 717px; height: 551px; }
  .offer-copy {
    position: absolute; left: 32px; top: 22px; width: 500px;
    color: var(--ink-light); font-weight: 400; font-size: 23.5px; line-height: 31.5px;
  }
  .offer-copy strong { font-weight: 700; }
  .offer-copy .indent { display: block; padding-left: 76px; }
  .logo-panel {
    position: absolute; left: 530px; top: 0; width: 148px; height: 160px;
    background: var(--card);
    display: flex; align-items: center; justify-content: center;
  }
  .logo-panel .brand-name { position: static; font-size: 24px; }
  .bubble--invite-dark { background: var(--slate); color: var(--brand-orange); left: 32px; top: 147px; width: 166px; height: 166px; font-size: 17px; }
  .bubble--date-warm { background: var(--brand-orange); color: var(--ink-light); left: 188px; top: 172px; width: 148px; height: 148px; font-size: 17px; }
</style>
</head>
<body>

  <section class="postcard postcard--address" aria-label="Postcard address side">
    <div class="brand-name">Bluebridge<br>care</div>
    <div class="bubble bubble--invite">Know more<br>about the<br>Monthly<br>Membership<br>Program</div>
    <div class="bubble bubble--date">Wednesday,<br>Feb. 18 drop<br>by between<br>6-8 pm</div>
    <div class="stamp-box">Place<br>Stamp<br>Here</div>
    <svg class="address-photo" viewBox="0 0 320 268" role="img" aria-label="Photo of a smiling doctor in a white coat beside a multi-generation family">
      <defs>
        <linearGradient id="groupTone" x1="0" y1="0" x2="1" y2="1">
          <stop offset="0" stop-color="var(--photo-light)"/>
          <stop offset="0.5" stop-color="var(--photo-cool)"/>
          <stop offset="1" stop-color="var(--photo-warm)"/>
        </linearGradient>
      </defs>
      <rect width="320" height="268" fill="url(#groupTone)"/>
    </svg>
    <div class="address-line" style="top:263px"></div>
    <div class="address-line" style="top:322px"></div>
    <div class="address-line" style="top:382px"></div>
  </section>

  <section class="postcard postcard--offer" aria-label="Postcard offer side">
    <svg class="offer-art" viewBox="0 0 717 551">
      <defs>
        <linearGradient id="familyTone" x1="0" y1="0" x2="1" y2="1">
          <stop offset="0" stop-color="var(--photo-light)"/>
          <stop offset="0.45" stop-color="var(--photo-warm)"/>
          <stop offset="1" stop-color="var(--photo-cool)"/>
        </linearGradient>
      </defs>
      <path class="offer-band" d="M0,0 H717 V160 C400,170 150,250 0,378 Z" fill="var(--brand-blue)"/>
      <g role="img" aria-label="Photo of a smiling family of five: father with son on his back, mother, and grandparents">
        <path d="M20,372 C160,262 400,182 700,170 V551 H20 Z" fill="url(#familyTone)"/>
      </g>
      <path class="offer-swoosh" d="M0,378 C150,250 400,170 717,160" fill="none" stroke="var(--brand-orange)" stroke-width="4"/>
    </svg>
    <p class="offer-copy">
      Monthly Membership Program for
      <span class="indent"><strong>$77</strong> per person, <strong>$167</strong> per family and</span>
      cover about <strong>85%</strong> of medical conditions.
      <span class="indent">Medical office visits are just $7 each.</span>
    </p>
    <div class="logo-panel"><div class="brand-name">Bluebridge<br>care</div></div>
    <div class="bubble bubble--invite-dark">Know more<br>about the<br>Monthly<br>Membership<br>Program</div>
    <div class="bubble bubble--date-warm">Wednesday,<br>Feb. 18 drop<br>by between<br>6-8 pm</div>
  </section>

</body>
</html>
```